Modern Medical Optometry Website

We need mordern, Patient friendly website. Easy to navigate and enhance our advance medical technology and excellent patient care.
1. HOME PAGE
2. OUR TEAM PAGE
3. EYECARE PAGE - VISION SERVICES, EYE EXAMS, KERATOCONUS CENTER, GLAUCOMA , DIABITES, TORVANEX EXAM, DIGITAL RETINAL, OCT.
4. MYOPIA CONTROL CLINIC
5. DRY EYE CLINIC
6. EYEWEAR
7. PATIENT CENTER - BLOG
7. CONTACT US
This is our current website www.brindlecove.com
and We want to add more content and a cleaner design like these website
http://tamsworthoptometry.com/
https://www.klmhaven.com/

```html
<!DOCTYPE html>
<html lang="en">
<head>
<meta charset="utf-8">
<title>Brindle Cove Optometry</title>
<link href="https://fonts.googleapis.com/css2?family=Ubuntu:wght@300;400;500;700&display=swap" rel="stylesheet">
<style>
:root{
  --blue:#00aeef;
  --teal:#1a8fb0;
  --link:#1f6fb5;
  --orange:#ef7a1f;
  --ink:#333;
  --muted:#666;
  --panel:#f3f3f1;
  --footer:#555555;
  --footer-dark:#474747;
  --footer-text:#e6e6e6;
  --footer-sub:#cfcfcf;
}
*{box-sizing:border-box;margin:0;padding:0}
html,body{width:1200px;height:1200px;overflow:hidden}
body{position:relative;font-family:'Ubuntu',sans-serif;background:#fff;color:var(--ink)}
.abs{position:absolute}

.services{left:0;top:0;width:610px;height:114px;background:#fff}
.services .tag{top:-2px;font-size:10px;color:var(--link)}
.btn-orange{left:297px;top:41px;width:124px;height:30px;background:var(--orange);color:#fff;font-size:10px;display:flex;align-items:center;justify-content:center;border-radius:2px}
.feature{top:0;height:114px;display:flex;align-items:flex-end;padding:0 0 22px 18px;color:#fff;font-weight:500;font-size:15px}
.feature.team{left:610px;width:291px;background:linear-gradient(180deg,#4b5a66,#2f3238)}
.feature.exam{left:901px;width:299px;background:linear-gradient(180deg,#8a6a58,#4a3a34);padding-left:19px}

.testimonials{left:0;top:114px;width:1200px;height:452px;background:var(--blue)}
.testimonials h2{position:absolute;top:30px;width:100%;text-align:center;color:#fff;font-weight:400;font-size:20px}
.card{left:235px;top:143px;width:732px;height:196px;background:#fff;text-align:center}
.avatar{left:546px;top:75px;width:112px;height:112px;border-radius:50%;border:3px solid #e5e5e5;background:linear-gradient(180deg,#e8edf0,#8fb3cc)}
.card .name{margin-top:52px;font-size:14px;font-weight:500;color:var(--teal)}
.card .role{font-size:11px;color:#777;margin-top:2px}
.card .q{font-size:14px;color:#555;line-height:12px;margin-top:2px}
.card p{font-size:9.5px;line-height:15px;color:#666;font-weight:300;padding:0 40px}
.arrow{top:226px;width:32px;height:32px}
.partners{top:363px;color:#fff;font-size:11px;text-align:center}
.badge{top:386px;height:30px}

.map{left:0;top:566px;width:817px;height:418px;background:linear-gradient(135deg,#d9e8d0,#ececec 40%,#e6e6e6 70%,#d6e6cc)}
.findus{left:817px;top:566px;width:383px;height:418px;background:var(--panel);padding:22px 0 0 18px}
.findus h3{font-size:19px;font-weight:400;color:var(--blue)}
.loc h4{font-size:12.5px;font-weight:400;color:#333;margin-top:12px}
.loc p{font-size:10px;color:#666;line-height:15px;margin-top:6px}
.dir{display:flex;margin-top:9px;height:18px;width:97px;font-size:9px}
.dir .pin{width:18px;background:#e6e6e6;display:flex;align-items:center;justify-content:center}
.dir .lbl{flex:1;background:#3b3b3b;color:#fff;display:flex;align-items:center;justify-content:center}
.sep{height:1px;width:253px;background:#ccc;margin-top:16px}

.footer{left:0;top:984px;width:1200px;height:180px;background:var(--footer)}
.col{top:42px}
.col .main{display:block;color:var(--footer-text);font-size:10px;margin-bottom:11.5px}
.col .sub{display:block;color:var(--footer-sub);font-size:8.5px;font-weight:300;line-height:15px}
.social{display:flex;align-items:center;color:var(--footer-text);font-size:8.5px;height:21.5px}
.social i{width:14px;height:14px;background:#ddd;border-radius:2px;margin-right:10px;display:inline-block}
.bottom{left:0;top:1164px;width:1200px;height:36px;background:var(--footer-dark);color:#cfcfcf;font-size:8.5px;display:flex;align-items:center;justify-content:center}
</style>
</head>
<body>

<section class="abs services">
  <span class="abs tag" style="left:165px">Eye Infections, Eye Injuries, Dry Eyes</span>
  <span class="abs tag" style="left:377px">Diabetic Screenings</span>
  <a class="abs btn-orange">View all our services</a>
</section>
<div class="abs feature team" role="img" aria-label="Photo of the clinic team">Best Team</div>
<div class="abs feature exam" role="img" aria-label="Photo of a child during an eye examination">Comprehensive Eye Examinations</div>

<section class="abs testimonials">
  <h2>Testimonials</h2>
  <div class="abs card">
    <div class="name">Dan Merrow</div>
    <div class="role">IT Employee</div>
    <div class="q">&ldquo;</div>
    <p>I want to recommend this Pharmacy to everybody. I have fought with my glaucoma for years using different optimetrist and specs but with these caps, I understood that what I need is just to eat less. I almost do not feel hunger and put off weight natural way.<br>I want to get to visit them again soon.</p>
  </div>
  <div class="abs avatar" role="img" aria-label="Portrait of the reviewer"></div>
  <svg class="abs arrow" style="left:153px" viewBox="0 0 32 32"><circle cx="16" cy="16" r="15" fill="none" stroke="#fff" stroke-width="1.5"/><path d="M18 10l-6 6 6 6" fill="none" stroke="#fff" stroke-width="1.5"/></svg>
  <svg class="abs arrow" style="left:1018px" viewBox="0 0 32 32"><circle cx="16" cy="16" r="15" fill="none" stroke="#fff" stroke-width="1.5"/><path d="M14 10l6 6-6 6" fill="none" stroke="#fff" stroke-width="1.5"/></svg>

  <div class="abs partners" style="left:295px;width:220px">Read more about us from here</div>
  <div class="abs badge" style="left:295px;width:106px;background:#fff" role="img" aria-label="Review listing badge"></div>
  <div class="abs badge" style="left:410px;width:106px;background:#ffee33" role="img" aria-label="Booking listing badge"></div>
  <div class="abs partners" style="left:670px;width:220px">We accept the Pell Credit Credit Card</div>
  <div class="abs badge" style="left:702px;width:154px;background:#fff" role="img" aria-label="Pell Credit payment badge"></div>
</section>

<div class="abs map" role="img" aria-label="Street map showing both clinic locations"></div>
<aside class="abs findus">
  <h3>Find Us</h3>
  <div class="loc">
    <h4>Brindle Cove Optometry</h4>
    <p>4120 Alder Row,<br>Fenwick, CA 90210</p>
    <p>Phone. 555-014-2010<br>Fax. 555-014-2070<br>Email. info@brindlecove.com</p>
    <a class="dir"><span class="pin"><svg width="8" height="10" viewBox="0 0 8 10"><path d="M4 0a4 4 0 0 1 4 4c0 3-4 6-4 6S0 7 0 4a4 4 0 0 1 4-4z" fill="#e53935"/></svg></span><span class="lbl">Get Directions</span></a>
  </div>
  <div class="sep"></div>
  <div class="loc">
    <h4 style="margin-top:16px">Harlow Park</h4>
    <p>8802 Quill Ave.,<br>Suite 4<br>Harlow Park, CA 90211</p>
    <p>Phone. 555-014-2010<br>Fax. 555-014-2070</p>
    <a class="dir"><span class="pin"><svg width="8" height="10" viewBox="0 0 8 10"><path d="M4 0a4 4 0 0 1 4 4c0 3-4 6-4 6S0 7 0 4a4 4 0 0 1 4-4z" fill="#e53935"/></svg></span><span class="lbl">Get Directions</span></a>
  </div>
</aside>

<footer class="abs footer">
  <nav class="abs col" style="left:161px">
    <a class="main">HOME</a><a class="main">OUR TEAM</a><a class="main">MYOPIA CONTROL CLINIC</a><a class="main">DRY EYE CLINIC</a>
  </nav>
  <nav class="abs col" style="left:386px">
    <a class="main" style="margin-bottom:6px">EYECARE</a>
    <a class="sub">VISION SERVICES</a><a class="sub">EYE EXAMS</a><a class="sub">KERATOCONUS CENTER</a><a class="sub">GLAUCOMA</a><a class="sub">DIABITES</a>
  </nav>
  <nav class="abs col" style="left:611px;top:58px">
    <a class="sub">TORVANEX EXAM</a><a class="sub">DIGITAL RETINAL OCT.</a>
    <a class="main" style="margin-top:12px">EYEWEAR</a><a class="main">CONTACT US</a>
  </nav>
  <div class="abs col" style="left:837px">
    <span class="main" style="margin-bottom:8px">Follow us</span>
    <a class="social"><i></i>Like on Friendwall</a>
    <a class="social"><i></i>Like on Snapgram</a>
    <a class="social"><i></i>View Circles</a>
    <a class="social"><i></i>See Rateline</a>
  </div>
</footer>
<div class="abs bottom">&copy; 2019 Brindlecove . All rights reserved.</div>

</body>
</html>
```